IT Services Business Card Design

We require a business card design for an IT services company called Tessaline.

We specialize in taking an organisations software and readying it for deployment to new environments (e.g. Zen qa to Zen 4). This process is termed application packaging. This is not the same as putting things in boxes but I am happy to use boxes as a pun icon ;-) This is our second step in branding, we currently have a new logo and our poor excuse of a website is next to be updated but it contains information on who we are and what we cover at rtprogramfreightworks.example

We are looking for a fun, modern but stylish and professional looking design.

I have attached the logo in multiple formats including vector formats (and the fonts that created the logo if required)
Updates

Thanks to all the designers so far, some great designs in there.  I will be selecting a card design on the deadline date. 

However, there is still time to submit some more designs.  The majority of the ones I have so far are typical simplistic designs that we have all seen before and I have enough of those to choose from now.  If you wish to submit any more designs, please submit somthing unusual to grab our attention.

Target Market(s)

Project executives of large organisations looking for Panecraft migrations

Industry/Entity Type

Software

Requirements
Must have
• Want to show company name, contact name, title, main number, contact number, fax number, email address and website address. I do not want to show the address.
Must use the attached logo, retaining the colours in them.

This has to be a double-sided design. I will be using lark.example and will be selecting their rounded corner business card design.

Their templates and design requirements (sizing etc.) can be found here: http://uk.lark.example/help/faq/templates-and-guidelines.html

Happy for company name or website to be on either side of the card.

This design has to be original and not used before for another company

Would like to style it around the business colours in the logo
Nice to have
• Lark.example has an option for multiple card designs to appear on the back. If this is possible in the budget and time you have and you have a design(s) that work with that but carry the same style and theme, that would be nice to see but not necessary.
Should not have
• We do not want to put a postal address on the cards

```html
<!DOCTYPE html>
<html lang="en">
<head>
<meta charset="utf-8">
<title>Tessaline – Business Card</title>
<link rel="stylesheet" href="https://fonts.googleapis.com/css2?family=Source+Sans+3:wght@400;600&display=swap">
<style>
  :root {
    --stage: #cccccc;
    --card-dark: #263029;
    --card-dark-edge: #e9e9e9;
    --card-light: #ffffff;
    --brand-blue: #4a72b8;
    --brand-brown: #6e665d;
    --mark-silver: #d6d8d8;
    --text-grey: #5e5a55;
  }
  * { margin: 0; padding: 0; box-sizing: border-box; }
  html, body {
    width: 872px; height: 1200px; overflow: hidden;
    background: var(--stage);
    font-family: "Source Sans 3", "Myriad Pro", sans-serif;
  }
  .canvas { position: relative; width: 872px; height: 1200px; }

  .card { position: absolute; }
  .card--back {
    left: 20px; top: 17px; width: 835px; height: 551px;
    background: var(--card-dark);
    border: 2px solid var(--card-dark-edge);
  }
  .card--front {
    left: 17px; top: 629px; width: 836px; height: 545px;
    background: var(--card-light);
  }

  .wordmark {
    position: absolute; font-weight: 400; font-size: 56px;
    line-height: 1; letter-spacing: 1px; white-space: nowrap;
  }
  .card--back .wordmark { right: 64px; top: 430px; color: var(--mark-silver); }
  .card--front .wordmark { left: 0; right: 0; text-align: center; top: 100px; color: var(--brand-brown); }

  .rule { position: absolute; left: 0; right: 0; height: 6px; background: var(--brand-brown); }
  .rule--upper { top: 249px; }
  .rule--lower { top: 316px; }
  .name-band {
    position: absolute; left: 0; right: 0; top: 262px; height: 47px;
    background: var(--brand-blue); color: #fff;
    display: flex; align-items: center; justify-content: center;
  }
  .name-band__name { font-weight: 600; font-size: 32px; }
  .name-band__title { font-weight: 400; font-size: 25px; margin-left: 6px; margin-top: 4px; }

  .contact-web {
    position: absolute; left: 150px; width: 270px; top: 386px;
    text-align: center; font-size: 23px; line-height: 33px; color: var(--text-grey);
  }
  .contact-web__site { color: var(--brand-blue); }
  .divider { position: absolute; left: 434px; top: 370px; width: 3px; height: 108px; background: var(--brand-blue); }
  .contact-phones {
    position: absolute; left: 471px; top: 369px;
    font-size: 24px; line-height: 35px; color: var(--text-grey); list-style: none;
  }
  .contact-phones__label { color: var(--brand-blue); }
</style>
</head>
<body>
<main class="canvas">
  <section class="card card--back" aria-label="Card back">
    <div class="wordmark">Tessaline</div>
  </section>

  <section class="card card--front" aria-label="Card front">
    <div class="wordmark">Tessaline</div>

    <div class="rule rule--upper"></div>
    <div class="name-band">
      <span class="name-band__name">Dana Morrow,</span>
      <span class="name-band__title">President</span>
    </div>
    <div class="rule rule--lower"></div>

    <div class="contact-web">
      <div>dana@quillstead.example</div>
      <div class="contact-web__site">www.Quillstead.example</div>
    </div>
    <div class="divider"></div>
    <ul class="contact-phones">
      <li><span class="contact-phones__label">M:</span> (555) 014-2290</li>
      <li><span class="contact-phones__label">C:</span> (555) 014-2290</li>
      <li><span class="contact-phones__label">F:</span> (555) 014-2290</li>
    </ul>
  </section>
</main>
</body>
</html>
```